Criação de Manual da Marca para Viagens & Lazer
A empresa queria:
" Funciona como o uBodal, mas para festas em geral, incluindo festas de pets. O responsável pela festa se cadastra, escolhe o tipo de festa (adulto, teen, infantil, chá de bebê, etc), insere as informações da festa e lança o site no ar. Acoplado a ele está uma lista de presentes ilustrada por produtos reais adequados ao tipo de festa e faixa etária do evento que são conversíveis em créditos. Não há entrega de produto, o total arrecadado é depositado na conta do cliente ou da instituição de caridade por ele indicada. "

```html
<!DOCTYPE html>
<html lang="pt-BR">
<head>
<meta charset="UTF-8">
<title>Manual de Marca — Presentia</title>
<link href="https://fonts.googleapis.com/css2?family=Open+Sans:wght@400;600;700&display=swap" rel="stylesheet">
<style>
  :root {
    --cover-red: #e5322b;
    --cover-orange: #f26f22;
    --cover-amber: #f5941f;
    --text-light: #ffffff;
    --brand-grey: #c8c8c8;
  }
  * { margin: 0; padding: 0; box-sizing: border-box; }
  html, body {
    width: 1200px;
    height: 1200px;
    overflow: hidden;
    background: #e9e9e9;
  }
  .cover {
    position: relative;
    width: 1200px;
    height: 1200px;
    overflow: hidden;
    background: linear-gradient(200deg, var(--cover-red) 0%, var(--cover-orange) 50%, var(--cover-amber) 100%);
    font-family: "Open Sans", sans-serif;
  }
  .cover-title {
    position: absolute;
    left: 84px;
    top: 70px;
    color: var(--text-light);
    font-weight: 700;
    font-size: 104px;
    line-height: 1.12;
    letter-spacing: 1px;
  }
  .brand {
    position: absolute;
    left: 700px;
    top: 700px;
    transform: translate(-50%, -50%);
    display: flex;
    flex-direction: column;
    align-items: center;
    gap: 36px;
  }
  .brand-mark {
    width: 150px;
    height: 150px;
    background: var(--brand-grey);
  }
  .brand-name {
    color: var(--brand-grey);
    font-weight: 600;
    font-size: 104px;
    line-height: 1;
  }
  .cover-subtitle {
    position: absolute;
    left: 60px;
    bottom: 60px;
    padding-left: 16px;
    border-left: 3px solid var(--text-light);
    color: var(--text-light);
    font-weight: 400;
    font-size: 32px;
    line-height: 1.15;
    text-transform: uppercase;
  }
</style>
</head>
<body>
  <main class="cover">
    <h1 class="cover-title">MANUAL<br>DE MARCA</h1>
    <div class="brand">
      <div class="brand-mark"></div>
      <div class="brand-name">Presentia</div>
    </div>
    <p class="cover-subtitle">Guia de identidade<br>visual</p>
  </main>
</body>
</html>
```